Business card design needed

I need a business card for a new company based in Perth, Western Australia, called KT Power Pty Ltd.

I'm the sole proprietor, and have 25 years' experience in directorship, senior commercial/business development/strategy roles in the oil & gas industry with both supermajors and junior listed companies. I also have interests in renewable energy (and am co-founder and director of a separate renewable energy start-up company). KT Power will be the vehicle for me to contract my services, principally in the oil & gas industry (although this will include directorship services to the renewable energy company). These services will include general consultancy in my areas of expertise, and contracting to provide senior management/director services to start-up or junior oil and gas companies.

I'm looking for a design that communicates professionalism, dynamism, experience, strategic skills and growth.

My Proflinker profile may also be useful context;

"I have a real passion for discovering new investment opportunities and turning them from talk into reality. Right now my focus is on oil, gas and energy ventures. I’m always on the look out for compelling new investment opportunities where I can bring my leadership and strategic insight to bear to make a real difference by delivering transformational results.

I spent 24 years with NX where I built up extensive international experience in oil, gas and energy and was a member of the company’s “fast track” development programme. As an entrepreneurial senior commercial leader, strategic thinker and tactical dealmaker I was responsible for numerous deals such as divestments, farm-ins, asset swaps, new acreage bids, unitizations, gas and LNG sales, creating billions of dollars of value for NX. These deals frequently broke new ground and/or required an innovative approach that delivered results in excess of what the business thought achievable. I have held senior executive and director roles covering Exploration & Production, Mergers & Acquisitions, Business Development, LNG Marketing, Joint Venture Management, Gas & Power and Corporate head office. International assignments included UK, Australia, Indonesia, Norway & Belgium.

I’m a member of the Guild of Global Fuel Brokers (GGFB) and the National Council of Board Officers (NCBO).

Board experience comprises four directorships and two alternate directorships of Australian companies, and directorship of a Not for Profit organisation.

Specialties
Strategy, Business Development, Mergers & Acquisitions, Joint Venture Management, Negotiation, Gas & LNG Marketing."

Target Market(s)

Oil and gas or energy companies of all sizes from large listed companies to start-ups - also service providers to the industry.

Industry/Entity Type

Oil And Gas

Contact Information for Business Card

KT Power Pty Ltd
Martin Dacombe
27C Ferncliff Road,
Holloway Vale,
WA 6999

Tel +61 400 555 817
email dacombemj@quenvol.example.au

```html
<!DOCTYPE html>
<html lang="en">
<head>
<meta charset="utf-8">
<title>KT Power Pty Ltd – Business Cards</title>
<link rel="stylesheet" href="https://fonts.googleapis.com/css2?family=Source+Sans+3:wght@300;400;700&display=swap">
<style>
  :root {
    --backdrop: #c8c8c8;
    --card: #ffffff;
    --ink: #231f20;
    --ink-soft: #3a3a3a;
    --paper-text: #ffffff;
    --shadow: rgba(0, 0, 0, 0.28);
  }
  * { box-sizing: border-box; margin: 0; padding: 0; }
  html, body {
    width: 1200px; height: 913px; overflow: hidden;
    background: var(--backdrop);
    font-family: "Source Sans 3", "Myriad Pro", Arial, sans-serif;
    color: var(--ink);
  }
  .stage { position: relative; width: 1200px; height: 913px; }

  .card {
    position: absolute;
    width: 465px; height: 270px;
    background: var(--card);
    box-shadow: 2px 3px 6px var(--shadow);
    overflow: hidden;
  }
  .card--single { left: 90px; top: 295px; }
  .card--front  { left: 655px; top: 172px; }
  .card--back   { left: 652px; top: 462px; }

  .company { font-weight: 700; font-size: 17px; letter-spacing: 0.1px; }
  .person  { font-weight: 700; font-size: 31px; line-height: 1; letter-spacing: -0.2px; }
  .contact { font-weight: 300; font-size: 14.5px; color: var(--ink-soft); }

  .card--single .company { position: absolute; left: 28px; top: 32px; }
  .card--single .person  { position: absolute; left: 27px; top: 60px; }
  .card--single .contact-block {
    position: absolute; right: 18px; top: 115px;
    text-align: right; line-height: 21.5px;
  }

  .card--front .contact-line {
    position: absolute; right: 16px; top: 32px;
    white-space: nowrap; text-align: right;
  }
  .card--front .contact-line span + span { margin-left: 16px; }
  .card--front .company-line {
    position: absolute; left: 20px; top: 52px; white-space: nowrap;
  }
  .card--front .company-line .contact { margin-left: 10px; }
  .card--front .person { position: absolute; left: 19px; top: 80px; }

  .oilfield-strip {
    position: absolute; left: 0; width: 100%; height: 36px;
    background: linear-gradient(to bottom, #ffffff 0%, #9a9a9a 55%, var(--ink) 100%);
  }
  .ground-band {
    position: absolute; left: 0; right: 0; bottom: 0;
    background: var(--ink);
  }

  .card--single .oilfield-strip { top: 180px; }
  .card--single .ground-band { top: 216px; padding: 7px 0 0 20px; }
  .card--front .oilfield-strip { top: 186px; }
  .card--front .ground-band { top: 222px; }
  .card--back .oilfield-strip { top: 192px; }
  .card--back .ground-band { top: 228px; }

  .services {
    font-weight: 700; font-size: 15px; line-height: 21px;
    letter-spacing: 0.4px; white-space: nowrap;
  }
  .services--reversed { color: var(--paper-text); }
  .card--back .services { position: absolute; left: 18px; top: 36px; }

  .caption {
    position: absolute;
    font-weight: 700; font-size: 28px; color: var(--paper-text);
    letter-spacing: 0.8px;
  }
  .caption--single { left: 90px; top: 602px; }
  .caption--double { left: 886px; top: 785px; }
</style>
</head>
<body>
<main class="stage">

  <section class="card card--single" aria-label="One-sided card">
    <p class="company">KT Power Pty Ltd</p>
    <h1 class="person">Martin Dacombe</h1>
    <div class="contact-block contact">
      <p>Tel +61 400 555 817</p>
      <p>email dacombemj@quenvol.example.au</p>
      <p>27C Ferncliff Road, Holloway Vale, WA 6999</p>
    </div>
    <div class="oilfield-strip" role="img" aria-label="Row of oil pump jack silhouettes along the horizon"></div>
    <div class="ground-band">
      <p class="services services--reversed">Strategy . Gas &amp; LNG Marketing . Joint Venture Management<br>Business Development . Mergers &amp; Acquisitions . Negotiation</p>
    </div>
  </section>

  <section class="card card--front" aria-label="Two-sided card, front">
    <p class="contact-line contact"><span>Tel +61 400 555 817</span><span>email dacombemj@quenvol.example.au</span></p>
    <p class="company-line"><span class="company">KT Power Pty Ltd</span><span class="contact">27C Ferncliff Road, Holloway Vale, WA 6999</span></p>
    <h2 class="person">Martin Dacombe</h2>
    <div class="oilfield-strip" role="img" aria-label="Row of oil pump jack silhouettes along the horizon"></div>
    <div class="ground-band"></div>
  </section>

  <section class="card card--back" aria-label="Two-sided card, back">
    <p class="services">Strategy . Gas &amp; LNG Marketing . Joint Venture Management<br>Business Development . Mergers &amp; Acquisitions . Negotiation</p>
    <div class="oilfield-strip" role="img" aria-label="Row of oil pump jack silhouettes along the horizon"></div>
    <div class="ground-band"></div>
  </section>

  <p class="caption caption--single">one-sided card</p>
  <p class="caption caption--double">two-sided card</p>

</main>
</body>
</html>
```